A taxi bidding business needs Web Design

We need a cutting edge, super UX-intuitive, Elegant web design for our business called Farovo.

Farovo is Australia based Kind of "Next Lyndo" business where user creates a trip and cabs/drivers place bids on fares/bookings/trips and lowest bidder gets the job.
User can also share the Cabs going in same route to get lowest bids.

- The design needs to be very, very intuitive to use and navigate. Please do not use much of yellow color.

References: StayMoor & Lyndo

Please see the attached pdf, attaching logo as well.

Target Market(s)

Ride Sharing, Taxi

Industry/Entity Type

Business

Number of Pages Required

5+ page

Requirements
Must have
• Icons/graphics, How it works icons, case studies icons, all mentioned pages
Should not have
• Not much yellow color

```html
<!DOCTYPE html>
<html lang="en">
<head>
<meta charset="utf-8">
<title>Farovo — Roam Around</title>
<link href="https://fonts.googleapis.com/css2?family=Open+Sans:wght@300;400;600;700&family=Roboto:wght@400;700&display=swap" rel="stylesheet">
<style>
:root{
  --topbar:#2b0f12;
  --navy:#10234f;
  --field:#0b1a3c;
  --field-line:#3a4f7d;
  --red:#ec1c24;
  --brown:#4a2a25;
  --ink:#1d2f6a;
  --grey:#6a6a6a;
  --icon-bg:#efefef;
  --icon:#4b4b4b;
  --white:#ffffff;
}
*{box-sizing:border-box;margin:0;padding:0}
html,body{width:1153px;height:1200px;overflow:hidden;background:var(--white);font-family:'Open Sans',sans-serif}
.page{position:relative;width:1153px;height:1200px}

.topbar{position:absolute;left:0;top:0;width:1153px;height:39px;background:var(--topbar);color:var(--white);font-size:14px}
.topbar a{position:absolute;top:9px;color:var(--white);text-decoration:none}
.menu-icon{position:absolute;left:71px;top:11px;width:25px;height:16px}
.menu-icon span{display:block;height:3px;background:var(--white);margin-bottom:3px}

.brand{position:absolute;left:84px;top:70px;width:145px;text-align:center}
.brand-dot{width:36px;height:36px;border-radius:50%;background:var(--red);margin:0 auto 14px}
.brand-name{font-weight:700;font-size:27px;letter-spacing:3px;color:var(--ink)}

.headline{position:absolute;left:338px;top:72px}
.headline h1{font-weight:300;font-size:59px;line-height:60px;color:var(--ink)}
.headline h2{font-weight:600;font-size:41px;line-height:44px;color:var(--brown)}
.headline-rule{position:absolute;left:776px;top:154px;width:295px;height:1px;background:#555}

.hero{position:absolute;left:71px;top:202px;width:1012px;height:318px;
  background:linear-gradient(100deg,#c9ad85 0%,#e3c9a3 35%,#b9a883 60%,#8c8f78 80%,#cdb594 100%)}

.signup{position:absolute;left:167px;top:475px;width:819px;height:393px;background:var(--navy);color:var(--white)}
.tab-rider{position:absolute;left:0;top:-1px;width:415px;height:46px;background:var(--red);display:flex;align-items:center}
.tab-rider svg{margin-left:18px}
.tab-rider .label{margin-left:12px;font-size:19px;font-weight:400}
.tab-rider .cta{position:absolute;right:37px;font-weight:700;font-size:14px}
.or-badge{position:absolute;left:397px;top:6px;width:32px;height:32px;border-radius:50%;background:var(--white);border:2px solid var(--navy);color:var(--navy);font-size:11px;font-weight:600;display:flex;align-items:center;justify-content:center}
.tab-driver{position:absolute;left:445px;top:6px;display:flex;align-items:center;font-size:20px;font-weight:300}
.tab-driver svg{margin-right:12px}

.field{position:absolute;height:35px;border:1px solid var(--field-line);background:var(--field);color:#b9c2d8;font-size:11px;padding:0 0 0 18px;display:flex;align-items:center}
.field.tall{height:49px;align-items:flex-start;padding-top:10px}

.submit{position:absolute;left:269px;top:253px;width:297px;height:34px;background:var(--red);display:flex;align-items:center;justify-content:space-between;padding:0 14px 0 20px;font-size:13.5px;font-weight:600}
.alt{position:absolute;left:0;top:298px;width:819px;text-align:center;font-size:10px}
.legal{position:absolute;left:0;top:318px;width:819px;text-align:center;font-size:8.4px;line-height:12.7px}

.feature{position:absolute;top:943px;width:300px;text-align:center}
.feature .icon{width:94px;height:86px;margin:0 auto;background:var(--icon-bg);display:flex;align-items:center;justify-content:center}
.feature h3{margin-top:22px;font-family:'Roboto',sans-serif;font-weight:700;font-size:13.5px;color:var(--ink)}
.feature .rule{width:66px;height:2px;background:var(--red);margin:8px auto 0}
.feature p{margin-top:15px;font-family:'Roboto',sans-serif;font-size:12.6px;line-height:16px;color:var(--grey)}
</style>
</head>
<body>
<div class="page">
  <header class="topbar">
    <div class="menu-icon"><span></span><span></span><span></span></div>
    <a style="left:167px">Ride</a>
    <a style="left:230px">Drive</a>
    <a style="left:948px">Help</a>
    <a style="left:1012px">Sign In</a>
  </header>

  <div class="brand">
    <div class="brand-dot"></div>
    <div class="brand-name">FAROVO</div>
  </div>

  <div class="headline">
    <h1>Roam Around</h1>
    <h2>Low Bids, lowest Fares</h2>
  </div>
  <div class="headline-rule"></div>

  <div class="hero" role="img" aria-label="Toy car resting on a vintage map with a location pin"></div>

  <section class="signup">
    <div class="tab-rider">
      <svg width="20" height="36" viewBox="0 0 20 36" fill="none" stroke="#fff" stroke-width="1.5"><rect x="3" y="2" width="12" height="22" rx="2"/><circle cx="9" cy="10" r="3"/><path d="M6 24c0 5 3 8 8 10"/></svg>
      <span class="label">Ride with FAROVO</span>
      <span class="cta">Sign Up &nbsp;&gt;</span>
    </div>
    <div class="or-badge">OR</div>
    <div class="tab-driver">
      <svg width="34" height="24" viewBox="0 0 34 24" fill="none" stroke="#fff" stroke-width="1.8"><path d="M2 14l4-7h14l5 7H2z"/><circle cx="8" cy="16" r="3"/><circle cx="26" cy="14" r="7"/><circle cx="26" cy="14" r="2"/></svg>
      <span>Sign up to drive</span>
    </div>

    <div class="field" style="left:34px;top:74px;width:363px">Fast Name</div>
    <div class="field" style="left:34px;top:117px;width:363px">Last Name</div>
    <div class="field" style="left:34px;top:159px;width:363px">Email</div>
    <div class="field" style="left:34px;top:203px;width:363px">Phone</div>
    <div class="field" style="left:417px;top:74px;width:363px">Create Password</div>
    <div class="field" style="left:417px;top:117px;width:363px">City</div>
    <div class="field tall" style="left:417px;top:187px;width:363px">Invite Code (optional)</div>

    <div class="submit"><span>SIGN UP TO DRIVE</span>
      <svg width="16" height="10" viewBox="0 0 16 10" fill="none" stroke="#fff" stroke-width="2"><path d="M0 5h14M10 1l4 4-4 4"/></svg>
    </div>
    <p class="alt">OR SIGN UP WITH YOUR RIDER ACCOUNT.</p>
    <p class="legal">By proceeding, I agree that Lyndo or its representatives may contact<br>me by email, phone, or SMS (including by automatic telephone<br>dialing system) at the email address or number I provide, including<br>for marketing purposes. I have read and understand the relevant Driver Privacy Statement.</p>
  </section>

  <div class="feature" style="left:89px">
    <div class="icon"><svg width="54" height="46" viewBox="0 0 54 46" fill="none" stroke="#4b4b4b" stroke-width="2.5"><path d="M8 4h26v30H8zM34 14h10l8 10v10H34"/><circle cx="14" cy="38" r="4"/><circle cx="42" cy="38" r="4"/><path d="M2 12h10M2 20h10M2 28h10"/></svg></div>
    <h3>INSTANT BIDS, SLASHED FARES</h3><div class="rule"></div>
    <p>Lorem ipsum dolor sit amet, consectetur adipiscing elit. Fusce vestibulum sagittis finibus. Phasellus tempor, lorem et egestas vulputate, nunc dolor luctus felis, ornare pellentesque nisl eros quis risus.</p>
  </div>
  <div class="feature" style="left:426px">
    <div class="icon"><svg width="56" height="50" viewBox="0 0 56 50" fill="#4b4b4b"><path d="M2 2h52v16h-6V8H8v10H2z"/><rect x="14" y="10" width="28" height="38" rx="2"/><rect x="30" y="14" width="8" height="30" fill="#efefef"/></svg></div>
    <h3>AUTOMATED BIDDING, SAVES TIME</h3><div class="rule"></div>
    <p>Lorem ipsum dolor sit amet, consectetur adipiscing elit. Fusce vestibulum sagittis finibus. Phasellus tempor, lorem et egestas vulputate, nunc dolor luctus felis, ornare pellentesque nisl eros quis risus.</p>
  </div>
  <div class="feature" style="left:764px">
    <div class="icon"><svg width="64" height="52" viewBox="0 0 64 52" fill="#4b4b4b"><path d="M4 24l6-12h26l6 12v14H4z"/><circle cx="12" cy="30" r="3" fill="#efefef"/><circle cx="34" cy="30" r="3" fill="#efefef"/><path d="M46 2l6 6-4 4 12 30-6 4-10-30-4 2-4-6z"/></svg></div>
    <h3>SPEEDY SERVICE ANYWHERE, ANYTIME</h3><div class="rule"></div>
    <p>Lorem ipsum dolor sit amet, consectetur adipiscing elit. Fusce vestibulum sagittis finibus. Phasellus tempor, lorem et egestas vulputate, nunc dolor luctus felis, ornare pellentesque nisl eros quis risus.</p>
  </div>
</div>
</body>
</html>
```